Zielgruppe
Beamer Vermietung
Aufgabenstellung
Erstellung 2 professionell aussehender Webseiten.
Projektor-Verleih-Region-Wendlar.de
sowie
Projektor-Verleih-Region-Haselfurtheim.de
Die Seiten sind aktuell im Betrieb, aber haben ein sehr veraltetes Design.
Die Seiten können ähnlich aussehen, sollten aber etwas unterschiedlich sein, damit sie für den Kunden leicht anders aussehen.
Wichtig ist, dass alle Seiten, inklusive Startseite, Unterseiten und Links designed werden und das dieses Design in die bestehende Wordpress Installation eingepflegt wird.
Es ist also notwendig, gute Wordpress Kenntnisse zu haben um dann auch zwei fertige Wordpress Seiten liefern zu können.

```html
<!DOCTYPE html>
<html lang="de">
<head>
<meta charset="utf-8">
<title>Projektor Verleih – Reservierung</title>
<link href="https://fonts.googleapis.com/css2?family=Roboto:wght@300;400;500;700&family=Roboto+Condensed:wght@400&display=swap" rel="stylesheet">
<style>
  :root {
    --navy: #2d3d57;
    --green: #9ac44b;
    --grey-band: #efefef;
    --topbar: #ebebeb;
    --text-grey: #6b6b6b;
    --white: #ffffff;
  }
  * { margin: 0; padding: 0; box-sizing: border-box; }
  html, body { width: 987px; height: 1200px; overflow: hidden; background: var(--white); }
  body { position: relative; font-family: "Roboto", sans-serif; color: var(--navy); }
  .abs { position: absolute; }

  .topbar { left: 0; top: 0; width: 987px; height: 25px; background: var(--topbar); border-bottom: 1px solid #d8d8d8; }
  .topbar-url { left: 134px; top: 7px; font-size: 8.5px; font-weight: 300; color: #444; }
  .social { top: 6px; width: 14px; height: 14px; border-radius: 50%; background: var(--navy); }
  .social.active { background: var(--green); }

  .site-title { left: 131px; top: 38px; font-family: "Roboto Condensed", sans-serif; font-size: 23px; color: var(--green); white-space: nowrap; }
  .meta-links { right: 133px; top: 46px; display: flex; align-items: center; gap: 15px; font-size: 10.5px; font-weight: 500; color: var(--navy); }
  .meta-links span { display: flex; align-items: center; gap: 8px; }

  .mainnav { left: 0; top: 83px; width: 987px; height: 39px; background: var(--navy); }
  .mainnav ul { list-style: none; position: absolute; left: 135px; top: 0; display: flex; height: 39px; }
  .mainnav li { padding: 0 7.5px; line-height: 39px; font-size: 12.3px; font-weight: 500; color: var(--white); white-space: nowrap; }
  .mainnav li.current { background: var(--green); color: var(--navy); }

  .hero { left: 0; top: 122px; width: 987px; height: 379px;
    background: linear-gradient(100deg, #5e5146 0%, #7a6a5b 30%, #a08a72 55%, #8f9aa2 75%, #6d7f8d 100%); }
  .hero-rule { left: 131px; top: 210px; width: 23px; height: 2px; background: var(--white); }
  .hero-title { left: 131px; top: 214px; font-size: 39.5px; font-weight: 700; line-height: 44px; color: var(--white); letter-spacing: -0.3px; white-space: nowrap; }
  .hero-sub { left: 132px; top: 306px; font-size: 23px; font-weight: 500; color: var(--white); white-space: nowrap; }
  .hero-button { left: 133px; top: 381px; width: 116px; height: 30px; border-radius: 15px; background: var(--green); color: var(--navy); font-size: 12px; font-weight: 500; text-align: center; line-height: 30px; }

  .title-band { left: 0; top: 501px; width: 987px; height: 69px; background: var(--grey-band); }
  .title-band h1 { position: absolute; left: 147px; top: 20px; font-size: 23.5px; font-weight: 700; color: var(--navy); white-space: nowrap; }
  .dot { border-radius: 50%; }

  .intro-heading { left: 0; top: 612px; width: 987px; text-align: center; font-size: 25px; font-weight: 500; color: var(--navy); }
  .intro-text { left: 211px; top: 685px; width: 565px; text-align: center; font-size: 13.5px; font-weight: 300; line-height: 22px; color: var(--text-grey); }

  .contact-card { left: 326px; top: 766px; width: 335px; height: 193px; background: var(--grey-band); }
  .contact-card .accent { position: absolute; left: 2px; top: 45px; width: 6px; height: 97px; background: var(--green); }
  .contact-card h2 { position: absolute; left: 76px; top: 46px; font-size: 17px; font-weight: 700; color: var(--navy); white-space: nowrap; }
  .contact-card p { position: absolute; left: 76px; top: 91px; font-size: 17px; font-weight: 300; line-height: 22px; color: var(--text-grey); white-space: nowrap; }

  .cta-footer { left: 0; top: 1022px; width: 987px; height: 139px; background: var(--navy); overflow: hidden; }
  .cta-footer h2 { position: absolute; left: 130px; top: 48px; font-size: 34px; font-weight: 500; color: var(--green); white-space: nowrap; }
  .cta-phone { position: absolute; right: 133px; top: 51px; display: flex; align-items: center; gap: 14px; font-size: 27px; font-weight: 300; color: var(--white); white-space: nowrap; }

  .copyright { left: 0; top: 1161px; width: 987px; height: 39px; background: var(--green); text-align: center; line-height: 39px; font-size: 9.5px; color: var(--navy); }
</style>
</head>
<body>

  <div class="abs topbar"></div>
  <div class="abs topbar-url">www.projektor-verleih-region-wendlar.de</div>
  <div class="abs social active" style="left:761px"></div>
  <div class="abs social" style="left:786px"></div>
  <div class="abs social" style="left:810px"></div>
  <div class="abs social" style="left:835px"></div>

  <div class="abs site-title">Beamer Vermietung zu Günstigen Konditionen</div>
  <div class="abs meta-links">
    <span>
      <svg width="16" height="11" viewBox="0 0 16 11"><rect x="0.6" y="0.6" width="14.8" height="9.8" fill="none" stroke="#2d3d57" stroke-width="1"/><polyline points="0.6,0.6 8,6.5 15.4,0.6" fill="none" stroke="#2d3d57" stroke-width="1"/></svg>
      Kontakt / Anreise
    </span>
    <span>Impressum</span>
  </div>

  <nav class="abs mainnav">
    <ul>
      <li>Startseite</li>
      <li>Beamer mieten</li>
      <li>HD-Beamer mieten</li>
      <li>Full HD-Beamer</li>
      <li>Leinwand mieten</li>
      <li class="current">Reservierung</li>
      <li>Preisliste</li>
      <li>Datenschutz</li>
    </ul>
  </nav>

  <div class="abs hero" role="img" aria-label="Foto eines Projektors auf einem Tisch in einem unscharfen Besprechungsraum"></div>
  <div class="abs hero-rule"></div>
  <div class="abs hero-title">&nbsp;! Beamer mieten zu<br>TOP-Konditionen !</div>
  <div class="abs hero-sub">NEU: Jetzt auch HD-Beamer!</div>
  <div class="abs hero-button">KONTAKT</div>

  <section class="abs title-band">
    <h1>Reservieren oder Buchen</h1>
  </section>
  <div class="abs dot" style="left:95px;top:533px;width:20px;height:20px;background:var(--green)"></div>
  <div class="abs dot" style="left:122px;top:522px;width:9px;height:9px;background:var(--navy)"></div>
  <div class="abs dot" style="left:751px;top:512px;width:50px;height:50px;background:var(--green)"></div>

  <h2 class="abs intro-heading">Sie haben Interesse an unserer Beamer Vermietung?</h2>
  <p class="abs intro-text">Dann rufen Sie uns einfach unter einer der unten stehenden Telefonnummern an und fragen Sie nach der Verfügbarkeit des gewünschten Beamers:</p>

  <div class="abs contact-card">
    <div class="accent"></div>
    <h2>Kroll Wenderath GbR</h2>
    <p>Festnetz: 02791/ 553042<br>Mobil: 0171 / 4408275</p>
  </div>

  <footer class="abs cta-footer">
    <h2>Reservieren oder Buchen</h2>
    <div class="cta-phone">
      <svg width="28" height="22" viewBox="0 0 28 22"><path d="M1 7 C1 1 27 1 27 7 L27 9 L20 9 L20 6 L8 6 L8 9 L1 9 Z" fill="#9ac44b"/><path d="M7 10 L21 10 L26 21 L2 21 Z" fill="#9ac44b"/><circle cx="14" cy="15" r="3" fill="#2d3d57"/></svg>
      Tel: 0171 / 2296014
    </div>
  </footer>

  <div class="abs copyright">Copyright © 2020.&nbsp; Projektor-verleih-region-wendlar.de</div>

</body>
</html>
```